New Web Site - Professional Cleaning Company

I want to create a new attractive website that acts as an advertisement to visitors to entice them to reach out for more information.
We are a commercial/business janitorial service - with a new logo, would like the font to be complimentary to the font of logo, as well as the color scheme.
Target Market(s)
Commercial buildings, schools & medical buildings
Industry/Entity Type
Janitorial
Coding
Coded - Design and coding required
Number of Pages Required
4 page
Requirements
Must have
- Professionalism, sharp imagery

```html
<!DOCTYPE html>
<html lang="en">
<head>
<meta charset="utf-8">
<title>Brightwell Facility Services</title>
<link href="https://fonts.googleapis.com/css2?family=Open+Sans:ital,wght@0,400;0,600;0,700;1,400;1,600&display=swap" rel="stylesheet">
<style>
:root{
  --blue:#1b9dd9;
  --navy:#0e2b78;
  --navy-dark:#0a1f5a;
  --grey-bg:#f1f1f1;
  --nav-bg:#ececec;
  --text:#222;
  --muted:#555;
  --green:#3aaa35;
}
*{box-sizing:border-box;margin:0;padding:0}
html,body{width:1200px;height:3855px;overflow:hidden}
body{font-family:"Open Sans",sans-serif;color:var(--text);position:relative;background:#fff}
.abs{position:absolute}
/* top bar */
.topbar{left:0;top:0;width:1200px;height:46px;background:var(--blue);color:#fff;font-size:11px}
.topbar .links{left:99px;top:16px;display:flex;gap:10px}
.topbar .links span{display:flex;align-items:center;gap:6px}
.topbar .links i{display:inline-block;width:12px;height:12px;border:1.5px solid #fff;border-radius:2px}
.topbar .addr{right:99px;top:16px;display:flex;align-items:center;gap:8px}
/* header */
.header{left:0;top:46px;width:1200px;height:114px;background:#fff}
.brand{left:97px;top:20px;display:flex;align-items:center;gap:10px}
.brand .mark{width:70px;height:70px;border-radius:50%;border:3px solid var(--blue)}
.brand .name{font-weight:700;color:var(--navy);font-size:15px;line-height:1.2;width:120px}
.pricing{left:716px;top:30px;font-style:italic;color:#888;font-size:15px;line-height:1.25}
.pricing b{color:var(--green);font-size:25px;font-style:normal}
.phone{left:940px;top:42px;display:flex;align-items:center;gap:6px;color:#888;font-size:21px}
/* nav */
.nav{left:0;top:160px;width:1200px;height:55px;background:var(--nav-bg);font-size:13px}
.nav a{position:absolute;top:20px;color:#222;text-decoration:none}
.nav .sep{position:absolute;top:18px;color:#444}
.nav .active{top:0;left:956px;width:145px;height:55px;background:var(--blue);color:#fff;text-align:center;line-height:55px}
/* hero */
.hero{left:0;top:215px;width:1200px;height:451px;background:linear-gradient(120deg,#dfe8ee 0%,#f4f6f7 40%,#e9d24a 55%,#f2f4f5 70%,#6fc0e6 100%)}
.hero .caption{left:99px;top:156px;width:380px;height:124px;background:rgba(140,140,140,.75);color:#fff;padding:28px 22px}
.hero .caption p{font-size:24px;line-height:1}
.hero .caption h2{font-size:31px;font-weight:700;line-height:1.1;margin-top:4px}
.arrow{width:34px;height:34px;border:2px solid #222;border-radius:50%;display:flex;align-items:center;justify-content:center}
/* about */
.about h2{left:98px;top:718px;font-size:30px;font-weight:400}
.about .lead{left:98px;top:757px;font-size:20px}
.about .copy{left:98px;top:798px;width:420px;font-size:12px;line-height:1.7;color:#333}
.about .copy b{color:var(--blue)}
.about .copy p+p{margin-top:18px}
.btn{background:var(--blue);color:#fff;font-size:13px;text-align:center}
.about .btn{left:97px;top:963px;width:168px;height:38px;line-height:38px}
.photo{display:block}
/* services */
.services{left:0;top:1119px;width:1200px;height:483px;background:var(--grey-bg)}
.section-title{width:1200px;text-align:center;font-size:28px;font-weight:400;color:#222}
.card{top:132px;width:230px;height:278px;color:#fff;text-align:center}
.card .label{position:absolute;left:0;right:0;bottom:22px;font-weight:600;font-size:18px;line-height:1.2}
.card.feature{background:#3d4c8c;padding:36px 12px 0}
.card.feature h3{font-size:18px;font-weight:600}
.card.feature p{font-size:11.5px;line-height:1.8;margin-top:6px}
/* handyman */
.list{font-size:15px;line-height:26px;color:#333;list-style:none}
.list li::before{content:"• "}
/* testimonials */
.testimonials{left:0;top:2301px;width:1200px;height:549px;background:var(--grey-bg)}
.tcard{top:197px;width:247px;height:274px;background:#e0e0e0;text-align:center;box-shadow:0 10px 12px -8px rgba(0,0,0,.25)}
.tcard .avatar{position:absolute;left:59px;top:-64px;width:128px;height:128px;border-radius:50%;border:6px solid #fff;background:linear-gradient(#d9c3ad,#9a8270)}
.tcard .quote{position:absolute;left:6px;top:-14px;font-size:60px;font-weight:700;color:var(--navy);font-family:Georgia,serif;line-height:1}
.tcard h4{margin-top:78px;font-size:16px;font-weight:400}
.tcard p{font-size:14px;line-height:1.35;color:#444;padding:8px 20px 0}
.tcard .role{position:absolute;left:0;right:0;bottom:0;height:37px;line-height:37px;background:var(--blue);color:#fff;font-size:11px;font-style:italic}
/* gallery */
.gphoto{width:266px;height:208px;border:3px solid #fff;box-shadow:0 0 4px rgba(0,0,0,.35)}
/* footer */
.footer{left:0;top:3500px;width:1200px;height:285px;background:var(--navy);color:#fff}
.footer h5{position:absolute;top:51px;font-size:16px;font-weight:400}
.footer h5::after{content:"";display:block;width:36px;height:2px;background:var(--blue);margin-top:8px}
.field{background:#fff;color:#888;font-size:10px;padding:4px 5px}
.footer .links{left:485px;top:101px;font-size:11.5px;line-height:25.5px;list-style:none}
.social{width:24px;height:24px;border-radius:50%}
.footer .contact{left:866px;top:101px;font-size:12px;line-height:22px}
.footer .contact .row{display:flex;gap:14px;margin-bottom:18px}
.bottombar{left:0;top:3785px;width:1200px;height:70px;background:var(--navy-dark);color:#fff;font-size:11px}
</style>
</head>
<body>

<div class="abs topbar">
  <div class="abs links"><span><i></i>Seasonal Check Ups</span><span>|</span><span><i></i>Schedule Repairs</span><span>|</span><span><i></i>24/7 Emergency Service</span></div>
  <div class="abs addr">
    <svg width="10" height="14" viewBox="0 0 10 14"><path d="M5 0a5 5 0 0 1 5 5c0 4-5 9-5 9S0 9 0 5a5 5 0 0 1 5-5z" fill="#fff"/><circle cx="5" cy="5" r="2" fill="#1b9dd9"/></svg>
    1234 1/2 Lakeview Ave, Fairhaven, CA 90000
  </div>
</div>

<div class="abs header">
  <div class="abs brand"><div class="mark"></div><div class="name">Brightwell Facility Services</div></div>
  <div class="abs pricing">GET PRICING AND <b>100%</b><br>FREE CONSULTATION NOW</div>
  <div class="abs phone">
    <svg width="16" height="34" viewBox="0 0 16 34"><path d="M12 2C5 4 2 10 2 17s3 13 10 15l3-6-4-2c-2-2-2-12 0-14l4-2z" fill="#aaa"/></svg>
    (555) 014-4009
  </div>
</div>

<nav class="abs nav">
  <a style="left:100px">HOME</a><span class="sep" style="left:186px">|</span>
  <a style="left:234px">ABOUT US</a><span class="sep" style="left:346px">|</span>
  <a style="left:394px">SERVICES</a><span class="sep" style="left:498px">|</span>
  <a style="left:547px">NEWS</a><span class="sep" style="left:630px">|</span>
  <a style="left:678px">GO GREEN</a><span class="sep" style="left:791px">|</span>
  <a style="left:839px">REFERENCES</a>
  <a class="active">CONTACT US</a>
</nav>

<section class="abs hero" role="img" aria-label="Gloved hand scrubbing a bathroom sink with a yellow sponge beside blue mosaic tiles">
  <div class="abs caption"><p>SERVING THE INDUSTRY FOR</p><h2>WELL OVER 2 YEARS</h2></div>
  <div class="abs arrow" style="left:13px;top:208px"><svg width="10" height="14"><path d="M8 1 2 7l6 6" stroke="#222" stroke-width="2" fill="none"/></svg></div>
  <div class="abs arrow" style="left:1154px;top:208px"><svg width="10" height="14"><path d="M2 1l6 6-6 6" stroke="#222" stroke-width="2" fill="none"/></svg></div>
</section>

<section class="about">
  <h2 class="abs">The reason we’ve been around</h2>
  <p class="abs lead">for so long is due to our unwavering focus and</p>
  <div class="abs copy">
    <p>commitment epitomized by one word: <b>Quality.</b> There is no room for shortcuts in our book, just delivery of our best performance to the highest standard. Needless to say, we take pride in what we do and aim to blow past your expectations of a janitorial company.</p>
    <p>We want to ensure you have peace of mind with <b>cleanliness</b> being the least of your worries, and our long history of happy clientele speak for us.</p>
  </div>
  <div class="abs btn">REQUEST ESTIMATES</div>
  <div class="abs photo" style="left:887px;top:712px;width:210px;height:210px;background:linear-gradient(135deg,#e0a24a,#f5d21a 55%,#c8902e)" role="img" aria-label="Hand holding a phone showing a we can help call us message"></div>
  <div class="abs photo" style="left:658px;top:836px;width:210px;height:210px;background:linear-gradient(160deg,#e6e9ec,#9aa8b8 60%,#2f5f9a)" role="img" aria-label="Technician servicing a ceiling air conditioning unit"></div>
</section>

<section class="abs services">
  <h2 class="abs section-title" style="top:56px">OUR SERVICES</h2>
  <div class="abs card" style="left:99px;background:linear-gradient(#e8ecef,#8aa7c7 60%,#1b9dd9)" role="img" aria-label="Janitor mopping a floor beside a cleaning cart"><div class="label">General Janitorial<br>Cleaning</div></div>
  <div class="abs card" style="left:356px;background:linear-gradient(#c44f9a,#8e6aa8 60%,#1b9dd9)" role="img" aria-label="Brush shampooing a patterned carpet"><div class="label">Carpet Shampoo</div></div>
  <div class="abs card feature" style="left:612px"><h3>Floor Waxing</h3><p>Floor waxing is a method of cleaning and polishing floors that not only gives them a renewed shine, but also helps to protect them from more damage. There are several different ways to wax different floor materials, and also several different products available for use on hard floor surfaces.</p></div>
  <div class="abs card" style="left:869px;background:linear-gradient(135deg,#6f9fd0,#cfe3f5 55%,#1b9dd9)" role="img" aria-label="Squeegee wiping a soapy window"><div class="label">Window Cleaning</div></div>
</section>

<section class="handyman">
  <h2 class="abs section-title" style="top:1648px">HANDYMAN</h2>
  <ul class="abs list" style="left:162px;top:1720px"><li>Install wall fixtures</li><li>Norvik furniture installation and assembly</li><li>Hanging mirrors, artwork</li></ul>
  <ul class="abs list" style="left:799px;top:1720px"><li>Furniture assembly</li><li>Stairs Restoration</li><li>Demolition</li></ul>
  <ul class="abs list" style="left:164px;top:1883px"><li>Shelf installation</li><li>Refinish Decks</li><li>Tv wall mounting</li></ul>
  <ul class="abs list" style="left:869px;top:1883px"><li>Tiling, Backsplash</li><li>Vanity installation</li><li>Caulking</li></ul>
  <ul class="abs list" style="left:164px;top:2045px"><li>Painting</li><li>Deck restoration</li><li>Drywall, taping and<br>&nbsp;&nbsp;patching installation</li></ul>
  <ul class="abs list" style="left:872px;top:2072px"><li>Cleaning ceiling fans</li><li>Switches and outlets</li><li>Drywall</li></ul>
  <svg class="abs" style="left:0;top:1780px" width="1200" height="480" viewBox="0 1780 1200 480">
    <path d="M585 1804 A226 226 0 0 0 585 2256" stroke="#1b9dd9" stroke-width="7" fill="none"/>
    <path d="M585 1804 A226 226 0 0 1 585 2256" stroke="#0e2b78" stroke-width="7" fill="none"/>
    <g stroke="#1b9dd9" stroke-width="3" fill="none">
      <path d="M162 1816H385l40 40"/><path d="M162 1976H305l40 40"/><path d="M162 2156H385l40 30"/>
    </g>
    <g stroke="#0e2b78" stroke-width="3" fill="none">
      <path d="M1041 1817H787l-40 40"/><path d="M1041 1978H850l-38 40"/><path d="M1041 2157H787l-40 30"/>
    </g>
    <g stroke="#fff" stroke-width="5">
      <polygon points="426,1826 464,1848 464,1892 426,1914 388,1892 388,1848" fill="#1b9dd9"/>
      <polygon points="359,1986 397,2008 397,2052 359,2074 321,2052 321,2008" fill="#1b9dd9"/>
      <polygon points="426,2143 464,2165 464,2209 426,2231 388,2209 388,2165" fill="#1b9dd9"/>
      <polygon points="746,1826 784,1848 784,1892 746,1914 708,1892 708,1848" fill="#0e2b78"/>
      <polygon points="812,1986 850,2008 850,2052 812,2074 774,2052 774,2008" fill="#0e2b78"/>
      <polygon points="746,2143 784,2165 784,2209 746,2231 708,2209 708,2165" fill="#0e2b78"/>
    </g>
    <g stroke="#fff" stroke-width="2" fill="none">
      <rect x="406" y="1856" width="40" height="28"/><path d="M406 1865h40M406 1875h40M416 1856v9M436 1856v9M426 1865v10M416 1875v9M436 1875v9"/>
      <path d="M340 2042h38M346 2042v-14M358 2042v-20M370 2042v-10"/>
      <rect x="412" y="2165" width="28" height="12"/><path d="M440 2171h6v12h-20v14"/>
      <path d="M728 1884h10v-8h10v-8h10v-8h10"/><circle cx="752" cy="1856" r="3"/>
      <path d="M790 2024h40v10h-40z M830 2029h10"/>
      <circle cx="746" cy="2187" r="4"/><path d="M746 2183v-16M742 2190l-14 8M750 2190l14 8"/>
    </g>
    <circle cx="585" cy="2030" r="92" fill="#fff"/>
    <circle cx="585" cy="2030" r="58" fill="none" stroke="#1b9dd9" stroke-width="4"/>
    <text x="585" y="2026" text-anchor="middle" font-family="Open Sans, sans-serif" font-weight="700" font-size="16" fill="#0e2b78">BRIGHTWELL</text>
    <text x="585" y="2046" text-anchor="middle" font-family="Open Sans, sans-serif" font-weight="700" font-size="9" fill="#0e2b78">FACILITY SERVICES</text>
  </svg>
</section>

<section class="abs testimonials">
  <h2 class="abs section-title" style="top:56px">TESTIMONIALS</h2>
  <div class="abs arrow" style="left:101px;top:313px"><svg width="10" height="14"><path d="M8 1 2 7l6 6" stroke="#222" stroke-width="2" fill="none"/></svg></div>
  <div class="abs arrow" style="left:1068px;top:313px"><svg width="10" height="14"><path d="M2 1l6 6-6 6" stroke="#222" stroke-width="2" fill="none"/></svg></div>
  <div class="abs tcard" style="left:175px"><span class="quote">“</span><div class="avatar" role="img" aria-label="Portrait of a client"></div><h4>Name Here</h4><p>Lorem Ipsum is simply dummy text of the printing and typesetting industry. Lorem Ipsum has been the industry's standard dummy text ever since the 1500s.</p><div class="role">Chief Technology Information Officer</div></div>
  <div class="abs tcard" style="left:479px"><span class="quote">“</span><div class="avatar" role="img" aria-label="Portrait of a client"></div><h4>Name Here</h4><p>Lorem Ipsum is simply dummy text of the printing and typesetting industry. Lorem Ipsum has been the industry's standard dummy text ever since the 1500s.</p><div class="role">Professor at Westbrook University</div></div>
  <div class="abs tcard" style="left:782px"><span class="quote">“</span><div class="avatar" role="img" aria-label="Portrait of a client"></div><h4>Name Here</h4><p>Lorem Ipsum is simply dummy text of the printing and typesetting industry. Lorem Ipsum has been the industry's standard dummy text ever since the 1500s.</p><div class="role">House wife</div></div>
</section>

<section class="gallery">
  <h2 class="abs section-title" style="top:2898px">OUR GALLERY</h2>
  <div class="abs gphoto" style="left:162px;top:2972px;background:linear-gradient(#e9edf0,#2b4fa0 60%,#e8ecef)" role="img" aria-label="Cleaner holding a bucket of supplies and a broom"></div>
  <div class="abs gphoto" style="left:468px;top:2972px;background:linear-gradient(135deg,#9a8c78,#e8e4de 50%,#3a6fa8)" role="img" aria-label="Floor scrubbing machine foaming a carpet"></div>
  <div class="abs gphoto" style="left:776px;top:2972px;background:linear-gradient(#4a4344,#c8c0bd 60%,#9a8e88)" role="img" aria-label="Mopping a shiny hallway floor"></div>
  <div class="abs gphoto" style="left:162px;top:3224px;background:linear-gradient(135deg,#f0f4f8,#3e86cc 55%,#1b5aa0)" role="img" aria-label="Window washer on a glass building facade"></div>
  <div class="abs gphoto" style="left:468px;top:3224px;background:linear-gradient(#3f86d4,#b8d4ee 55%,#8b6a3c)" role="img" aria-label="Worker with tool belt in front of a house"></div>
  <div class="abs gphoto" style="left:776px;top:3224px;background:linear-gradient(135deg,#d9dde2,#3c5c98 55%,#e6e6e6)" role="img" aria-label="Plumber with tools in a kitchen"></div>
</section>

<footer class="abs footer">
  <h5 style="left:102px">SEND MESSAGE</h5>
  <div class="abs field" style="left:102px;top:96px;width:137px;height:24px">NAME</div>
  <div class="abs field" style="left:248px;top:96px;width:144px;height:24px">EMAIL</div>
  <div class="abs field" style="left:102px;top:132px;width:290px;height:73px">MESSAGE</div>
  <div class="abs btn" style="left:272px;top:214px;width:120px;height:34px;line-height:34px;font-size:11px">SEND MESSAGE</div>

  <h5 style="left:485px">SITE LINKS</h5>
  <ul class="abs links"><li>HOME</li><li>ABOUT US</li><li>SERVICES</li><li>NEWS</li><li>GO GREEN</li><li>CONTACT</li></ul>

  <h5 style="left:673px;top:48px">FOLLOW US</h5>
  <div class="abs social" style="left:673px;top:98px;background:#3b5fa8"></div>
  <div class="abs social" style="left:706px;top:98px;background:#2fa6e0"></div>
  <div class="abs social" style="left:739px;top:98px;background:#b07a52"></div>
  <div class="abs social" style="left:673px;top:144px;background:#d63b2e"></div>
  <div class="abs social" style="left:706px;top:144px;background:#d1463a"></div>
  <div class="abs social" style="left:739px;top:144px;background:#1a7bb8"></div>

  <h5 style="left:866px">CONTACT US</h5>
  <div class="abs contact">
    <div class="row"><svg width="12" height="16" viewBox="0 0 10 14"><path d="M5 0a5 5 0 0 1 5 5c0 4-5 9-5 9S0 9 0 5a5 5 0 0 1 5-5z" fill="#1b9dd9"/></svg><span>1234 1/2 Lakeview Ave,<br>Fairhaven, CA 90000</span></div>
    <div class="row"><svg width="12" height="14" viewBox="0 0 12 14"><path d="M2 1l3 3-2 2c1 2 3 4 5 5l2-2 3 3-2 2C5 13 0 8 0 3z" fill="#1b9dd9"/></svg><span>(555) 623-0199</span></div>
    <div class="row"><svg width="14" height="12" viewBox="0 0 14 12"><rect width="14" height="12" fill="#1b9dd9"/><path d="M0 0l7 6 7-6" stroke="#0e2b78" fill="none"/></svg><span>info@brightwellfs.example<br>Mon - Thur: 8:00 am - 5:00 pm<br>Sat - Sun: 12:00 pm - 3:00 pm</span></div>
  </div>
</footer>

<div class="abs bottombar">
  <div class="abs" style="left:102px;top:31px">Copyright © 2022 Brightwell Facility Services, All rights reserved.</div>
  <div class="abs" style="left:1076px;top:27px;width:25px;height:25px;background:var(--blue);display:flex;align-items:center;justify-content:center"><svg width="12" height="8"><path d="M1 7l5-5 5 5" stroke="#fff" stroke-width="2" fill="none"/></svg></div>
</div>

</body>
</html>
```